Design mobile friendly real estate and property management company landing page

Design a clean, crisp modern looking landing page that is mobile-friendly (must resize, preferably using bootstrap framework). Landing page will consist of heading with login area, company info, body consists of company description and services, a list of available rental properties with photos, and a footer with additional links and info. Working on updating with text for text areas marked A, B, and C on the layout pdf, but in meantime, lorem ipsum is fine. I can connect events to most buttons, etc. Just need the bootstrap and html functionality set up. Previous company website (which should not be relied upon) is www.qlbt.net This is somewhat of a template for a start, but looking for a more professional and modern design for the new website. But this gives an idea of the content and what needs to be displayed, and how.

Target Market(s)

Clients looking for a property management company that is efficient and well-organized.

Industry/Entity Type

Property Management

Coding

Coded - Design and coding required

Number of Pages Required

1 page

Font styles to use
Sans Serif

Colors
0355a3

Requirements
Must have
• Resize for the screen using bootstrap.
• Navigation that collapses for mobile devices
• Large text boxes and good solid spacing around all elements.
Nice to have
• for property images it would be nice if they can be swiped on touch enabled devices (to the next or previous image). And have navigation that can be clicked to next or previous images.
• Would be nice if a captcha verification was included on contact form.
Should not have
• Fancy or eccentric art

```html
<!DOCTYPE html>
<html lang="en">
<head>
<meta charset="utf-8">
<title>Northvale Realty Services</title>
<link rel="stylesheet" href="https://fonts.googleapis.com/css2?family=Open+Sans:ital,wght@0,400;0,600;0,700;1,400&display=swap">
<style>
:root{
  --brand:#0355a3;
  --brand-dark:#02468a;
  --ink:#222;
  --text:#555;
  --muted:#8a8a8a;
  --white:#fff;
  --footer:#0d0d0d;
  --footer-line:#2a2a2a;
  --footer-text:#9a9a9a;
  --field:#1c1c1c;
  --panel:#f7f7f7;
}
*{box-sizing:border-box;margin:0;padding:0}
html,body{width:1200px;height:2242px;overflow:hidden}
body{font-family:"Open Sans",Arial,sans-serif;color:var(--text);background:var(--white);position:relative}
.wrap{width:702px;margin:0 auto;position:relative}

/* header */
.site-header{height:55px}
.site-header .wrap{display:flex;justify-content:space-between;align-items:center;height:55px}
.brand{display:flex;align-items:center;gap:8px;font-size:17px;font-weight:700;color:var(--ink);letter-spacing:.5px;text-transform:uppercase}
.brand-mark{width:14px;height:14px;background:var(--brand)}
.social{display:flex;gap:5px}
.social span{display:block;width:21px;height:21px;background:var(--brand);border-radius:2px}

/* nav */
.main-nav{height:32px;background:var(--brand)}
.main-nav ul{list-style:none;display:flex;justify-content:center;height:32px;align-items:center}
.main-nav li{color:var(--white);font-size:12px;padding:0 16px}

/* hero */
.hero{height:346px;position:relative;background:linear-gradient(180deg,#b9cbe0 0%,#d8c8a8 45%,#8a7458 75%,#4f6b2e 100%)}
.hero-caption{position:absolute;left:654px;top:145px;width:296px;height:164px;background:rgba(255,255,255,.88)}
.caption-head{display:flex;align-items:center;height:26px}
.price{background:var(--brand);color:var(--white);font-size:14px;font-weight:600;height:26px;line-height:26px;padding:0 28px 0 12px;clip-path:polygon(0 0,100% 0,82% 100%,0 100%)}
.caption-title{color:var(--brand);font-size:20px;font-weight:600;margin-left:6px}
.caption-text{font-size:10px;line-height:14px;color:#444;text-align:center;padding:8px 10px 0}
.btn{display:inline-block;background:var(--brand);color:var(--white);font-size:12px;text-align:center;border-bottom:3px solid var(--brand-dark)}
.hero-caption .btn{position:absolute;left:96px;top:122px;width:104px;height:30px;line-height:28px;text-transform:uppercase}
.dots{display:flex;gap:5px;justify-content:center}
.dots i{width:7px;height:7px;border-radius:50%;border:1px solid var(--brand);display:block}
.dots i.on{background:var(--brand)}
.hero .dots{position:absolute;top:333px;left:0;right:0}

/* services band */
.services{height:178px;background:var(--brand);color:var(--white)}
.services .wrap{display:flex;justify-content:space-between;width:736px}
.service{width:232px;text-align:center;padding-top:11px}
.service-icon{width:60px;height:60px;margin:0 auto;border:2px solid var(--white);border-radius:50%;display:flex;align-items:center;justify-content:center}
.service h3{font-size:13px;font-weight:600;margin-top:11px}
.service p{font-size:9.5px;line-height:13.5px;margin-top:5px;color:#e6eef8}

/* feature properties */
.features{padding-top:16px;height:347px}
.section-bar{display:flex;justify-content:space-between;align-items:center;height:31px}
.bar-title{display:flex;align-items:center;justify-content:space-between;width:201px;height:31px;background:#222;color:var(--white);font-size:18px;padding:0 8px 0 7px}
.arrows{display:flex;gap:3px}
.arrows span{width:21px;height:23px;background:var(--brand);display:flex;align-items:center;justify-content:center}
.cards{display:flex;justify-content:space-between;margin-top:14px}
.card{width:228px;height:272px}
.card-villa{background:linear-gradient(180deg,#8fb8e6 0%,#e8ecef 50%,#4aa6d8 85%,#2d86bd 100%)}
.card-house{background:linear-gradient(180deg,#5b9ee2 0%,#9fb6c9 40%,#b7a57b 70%,#6f8a4a 100%)}
.card-rent{background:var(--brand);padding:9px}
.card-rent .frame{border:2px solid rgba(255,255,255,.75);height:100%;text-align:center;color:var(--white);padding-top:42px}
.card-rent h3{font-size:20px;font-weight:400}
.card-rent p{font-size:9.5px;line-height:15px;padding:8px 14px 0}
.card-rent .ghost{display:inline-block;margin-top:14px;border:1px solid var(--white);font-size:11.5px;padding:5px 12px;text-transform:uppercase}

/* agent */
.agent{height:306px}
.agent .wrap{display:flex;justify-content:space-between}
.agent-photo{width:290px;height:290px;border-radius:50%;background:radial-gradient(circle at 40% 40%,#e9e5e1 0%,#c9c1b9 55%,#2f2f33 100%)}
.agent-info{width:400px}
.agent-bar{display:flex;justify-content:space-between;align-items:center;height:36px;background:var(--brand);color:var(--white);font-size:16px;font-weight:600;padding:0 10px 0 8px}
.agent-info .intro{font-size:11px;line-height:16px;padding:14px 10px 0 11px;color:#444}
.contact-row{display:flex;gap:12px;padding-left:11px;margin-top:16px}
.contact-row svg{flex:none;margin-top:3px}
.contact-row h4{font-size:13px;font-weight:600;color:var(--ink)}
.contact-row p{font-size:10.5px;color:var(--muted);margin-top:2px}
.agent .btn{margin:16px 0 0 11px;width:104px;height:30px;line-height:28px}

/* testimonial */
.testimonial{height:331px;background:linear-gradient(120deg,#f4f4f4 0%,#e4e6ea 45%,#eff0f2 100%);text-align:center;padding-top:10px}
.testimonial h2{color:var(--brand);font-size:18px;font-weight:600}
.quote{font-size:46px;line-height:30px;color:#9a9a9a;font-weight:700;height:30px;margin-top:4px}
.client-photo{width:138px;height:138px;border-radius:50%;margin:4px auto 0;background:radial-gradient(circle at 50% 40%,#d9d9d9 0%,#a9a9ac 60%,#3a3d44 100%);border:3px solid var(--white)}
.client-name{color:var(--brand);font-size:18px;margin-top:8px}
.client-quote{width:600px;margin:0 auto;font-size:11px;line-height:15px;font-style:italic;color:#666}
.testimonial .dots{margin-top:15px}

/* info columns */
.info{height:330px;padding-top:12px}
.info .wrap{display:flex;justify-content:space-between}
.info-col{width:229px}
.info-col h2{color:var(--brand);font-size:17px;font-weight:600;height:29px}
.info-card{background:var(--panel);border:1px solid #ececec;height:272px}
.info-img{height:120px}
.img-blog{background:linear-gradient(180deg,#9cc0e0 0%,#c7b08e 55%,#6d7a3b 100%)}
.img-work{background:linear-gradient(180deg,#eef1f4 0%,#cdbfae 50%,#3c4250 100%)}
.img-why{background:linear-gradient(180deg,#dfe8f2 0%,#a9b8ca 55%,#56657a 100%)}
.info-card h3{color:var(--brand);font-size:14.5px;font-weight:400;padding:7px 7px 0}
.info-card p{font-size:10px;line-height:14.5px;color:#444;padding:3px 7px 0}
.info-card .btn{margin:10px 0 0 7px;width:104px;height:30px;line-height:28px}

/* footer */
.site-footer{height:317px;background:var(--footer);position:relative}
.footer-cols{display:flex;padding-top:48px}
.footer-col{width:181px;padding-right:14px}
.footer-col:last-child{width:159px;padding-right:0}
.footer-brand{color:var(--white);font-size:14px;font-weight:600;text-transform:uppercase;display:flex;align-items:center;gap:6px;height:22px}
.footer-brand .brand-mark{width:10px;height:10px}
.footer-about{font-size:9px;line-height:13px;color:#555;margin-top:6px}
.footer-col .social{margin-top:12px}
.footer-col h4{color:var(--white);font-size:11px;font-weight:400;text-transform:uppercase;padding-bottom:8px;border-bottom:1px solid var(--footer-line)}
.link-list{list-style:none}
.link-list li{font-size:9.5px;color:var(--footer-text);height:24px;line-height:23px;border-bottom:1px solid var(--footer-line)}
.link-list li.current{color:var(--white)}
.field{background:var(--field);height:20px;margin-top:6px;font-size:9px;color:#555;padding:4px 8px}
.field:first-of-type{margin-top:10px}
.field.area{height:54px}
.site-footer .submit{width:104px;height:30px;line-height:28px;margin-top:6px;text-transform:uppercase}
.touch-lead{font-size:9.5px;line-height:13px;color:#cfcfcf;font-weight:600;margin-top:10px}
.touch-row{display:flex;gap:9px;font-size:9px;line-height:12px;color:var(--footer-text);padding:8px 0;border-bottom:1px solid var(--footer-line)}
.touch-row svg{flex:none;margin-top:1px}
.copyright{position:absolute;left:249px;bottom:0;width:702px;height:31px;background:var(--brand);color:#dce8f5;font-size:9px;line-height:31px;padding:0 18px}
</style>
</head>
<body>

<header class="site-header">
  <div class="wrap">
    <div class="brand"><span class="brand-mark"></span>Northvale Realty Services</div>
    <div class="social" aria-label="Social links"><span></span><span></span><span></span><span></span></div>
  </div>
</header>

<nav class="main-nav">
  <ul>
    <li>Home</li><li>About</li><li>Services</li><li>Properties for Rent</li><li>Properties for Sale</li><li>Blog</li><li>Contact Us</li>
  </ul>
</nav>

<section class="hero" role="img" aria-label="Large two-storey brick family house with bay windows, lawn and garden under a blue sky">
  <div class="hero-caption">
    <div class="caption-head"><span class="price">$560,000</span><span class="caption-title">Dupplex 415 Elm</span></div>
    <p class="caption-text">Lorem Ipsum is simply dummy text of the printing and typesetting industry. Lorem Ipsum has been the industry's standard dummy text ever since the 1500s, when anunknown printer took a galley of type and scrambled it to make a type specimen book. It has survived not only five centuries, but</p>
    <span class="btn">View Details</span>
  </div>
  <div class="dots"><i></i><i class="on"></i><i></i><i></i></div>
</section>

<section class="services">
  <div class="wrap">
    <div class="service">
      <div class="service-icon">
        <svg width="32" height="28" viewBox="0 0 32 28" fill="none" stroke="#fff" stroke-width="2"><path d="M3 14 16 3l13 11"/><path d="M7 11v14h18V11"/><rect x="13" y="17" width="6" height="8"/></svg>
      </div>
      <h3>House For Rent And Sale</h3>
      <p>Lorem Ipsum is simply dummy text of the printing and typesetting industry. Lorem Ipsum has been the industry's standard dummy unknown printer took a galley of type and scrambled</p>
    </div>
    <div class="service">
      <div class="service-icon">
        <svg width="30" height="30" viewBox="0 0 30 30" fill="none" stroke="#fff" stroke-width="2"><path d="M6 16a9 9 0 0 1 18 0"/><rect x="4" y="15" width="5" height="8" rx="2" fill="#fff"/><rect x="21" y="15" width="5" height="8" rx="2" fill="#fff"/><path d="M24 23c0 3-4 4-8 4"/></svg>
      </div>
      <h3>Customer Care</h3>
      <p>Lorem Ipsum is simply dummy text of the printing and typesetting industry. Lorem Ipsum has been the industry's standard dummy unknown printer took a galley of type and scrambled</p>
    </div>
    <div class="service">
      <div class="service-icon">
        <svg width="30" height="30" viewBox="0 0 30 30"><circle cx="15" cy="15" r="12" fill="#fff"/><circle cx="15" cy="9" r="2" fill="#0355a3"/><rect x="13.3" y="12.5" width="3.4" height="10" fill="#0355a3"/></svg>
      </div>
      <h3>Information About House</h3>
      <p>Lorem Ipsum is simply dummy text of the printing and typesetting industry. Lorem Ipsum has been the industry's standard dummy unknown printer took a galley of type and scrambled</p>
    </div>
  </div>
</section>

<section class="features">
  <div class="wrap">
    <div class="section-bar">
      <div class="bar-title">Feature Properties
        <svg width="16" height="14" viewBox="0 0 16 14"><path d="M8 1 1 7h2v6h4V9h2v4h4V7h2z" fill="#0355a3"/></svg>
      </div>
      <div class="arrows">
        <span><svg width="10" height="14" viewBox="0 0 10 14" fill="none" stroke="#fff" stroke-width="2"><path d="M8 1 2 7l6 6"/></svg></span>
        <span><svg width="10" height="14" viewBox="0 0 10 14" fill="none" stroke="#fff" stroke-width="2"><path d="m2 1 6 6-6 6"/></svg></span>
      </div>
    </div>
    <div class="cards">
      <div class="card card-villa" role="img" aria-label="Modern white villa with a blue swimming pool"></div>
      <div class="card card-rent">
        <div class="frame">
          <h3>House For Rent</h3>
          <p>Lorem Ipsum is simply dummy text of the printing and typesetting industry. Lorem Ipsum has been the industry's standard dummy text ever since the 1500s, when an unknown printer took a galley of type and scrambled it to make a type specimen book.</p>
          <span class="ghost">View Details</span>
        </div>
      </div>
      <div class="card card-house" role="img" aria-label="Two-storey suburban house with gabled roof and flowering tree"></div>
    </div>
  </div>
</section>

<section class="agent">
  <div class="wrap">
    <div class="agent-photo" role="img" aria-label="Portrait of the property agent in a dark business suit"></div>
    <div class="agent-info">
      <div class="agent-bar">Agent Profile
        <svg width="14" height="14" viewBox="0 0 14 14" fill="#c9d9ec"><circle cx="7" cy="4" r="3.3"/><path d="M1 14c0-4 3-6 6-6s6 2 6 6z"/></svg>
      </div>
      <p class="intro">Lorem Ipsum is simply dummy text of the printing and typesetting industry. Lorem Ipsum has been the industry's standard dummy text ever since the 1500s, when an unknown printer took a galley</p>
      <div class="contact-row">
        <svg width="13" height="10" viewBox="0 0 13 10"><rect width="13" height="10" rx="1" fill="#0355a3"/><path d="m1 1 5.5 4.5L12 1" stroke="#fff" fill="none"/></svg>
        <div><h4>Email</h4><p>Harbor Point Office, 52 Linden Row, 20417 Eastfield</p></div>
      </div>
      <div class="contact-row">
        <svg width="13" height="13" viewBox="0 0 13 13"><path d="M3 0 5 3 3.5 4.5c.8 2 2.5 3.7 4.5 4.5L9.5 7.5 13 9.5 12 12C6 12 1 7 1 1z" fill="#0355a3"/></svg>
        <div><h4>Phone</h4><p>0412-3307-62918</p></div>
      </div>
      <div class="contact-row">
        <svg width="13" height="14" viewBox="0 0 12 16"><path d="M6 0a6 6 0 0 0-6 6c0 4 6 10 6 10s6-6 6-10a6 6 0 0 0-6-6z" fill="#0355a3"/><circle cx="6" cy="6" r="2.2" fill="#fff"/></svg>
        <div><h4>Address</h4><p>Harbor Point Office, 52 Linden Row, 20417 Eastfield</p></div>
      </div>
      <span class="btn">Contact Now</span>
    </div>
  </div>
</section>

<section class="testimonial" role="img" aria-label="Faint background of two people shaking hands">
  <h2>Testimonial Client</h2>
  <div class="quote">&#8221;</div>
  <div class="client-photo" role="img" aria-label="Portrait of the client wearing glasses"></div>
  <div class="client-name">Elias</div>
  <p class="client-quote">Lorem Ipsum is simply dummy text of the printing and typesetting industry. Lorem Ipsum has been the industry's standard dummy text ever since the 1500s, when an unknown printer took a galley of type and scrambled it to make a type specimen book.Lorem Ipsum is simply dummy text of the printing and typesetting industry. Lorem Ipsum has been the industry's</p>
  <div class="dots"><i></i><i class="on"></i><i></i></div>
</section>

<section class="info">
  <div class="wrap">
    <div class="info-col">
      <h2>Blog</h2>
      <div class="info-card">
        <div class="info-img img-blog" role="img" aria-label="Stone villa with a tiled roof and front garden"></div>
        <h3>What is Good Properties</h3>
        <p>Lorem Ipsum is simply dummy text of the printing and typesetting industry. Lorem Ipsum has been the industry's standard dummy text ever since the 1500s, when an unknown printer took a galley of type and scrambled it to make a type specimen book.</p>
        <span class="btn">View More</span>
      </div>
    </div>
    <div class="info-col">
      <h2>How We Work</h2>
      <div class="info-card">
        <div class="info-img img-work" role="img" aria-label="Smiling team of colleagues in business attire"></div>
        <h3>How We Work</h3>
        <p>Lorem Ipsum is simply dummy text of the printing and typesetting industry. Lorem Ipsum has been the industry's standard dummy text ever since the 1500s, when an unknown printer took a galley of type and scrambled it to make a type specimen book.</p>
        <span class="btn">View More</span>
      </div>
    </div>
    <div class="info-col">
      <h2>Why Choose Us</h2>
      <div class="info-card">
        <div class="info-img img-why" role="img" aria-label="Business handshake in a bright office"></div>
        <h3>Why Choose Us</h3>
        <p>Lorem Ipsum is simply dummy text of the printing and typesetting industry. Lorem Ipsum has been the industry's standard dummy text ever since the 1500s, when an unknown printer took a galley of type and scrambled it to make a type specimen book.</p>
        <span class="btn">View More</span>
      </div>
    </div>
  </div>
</section>

<footer class="site-footer">
  <div class="wrap footer-cols">
    <div class="footer-col">
      <div class="footer-brand"><span class="brand-mark"></span>Northvale Realty</div>
      <p class="footer-about">Lorem ipsum dolor sit amet, consectetuer adipiscing elit, sed diam nonummy nibh euismod tincidunt ut laoreet dolore magna aliquam erat. Eodem modo typi, qui nunc nobis videntur parum clari, fiant sollemnes in futurum. Claritas est etiam processus dynamicus.</p>
      <div class="social"><span></span><span></span><span></span><span></span></div>
    </div>
    <div class="footer-col">
      <h4>User Links</h4>
      <ul class="link-list">
        <li>&#8250; Help Center</li>
        <li class="current">&#8250; Properties for Rent</li>
        <li>&#8250; Properties for Sale</li>
        <li>&#8250; Blog</li>
        <li>&#8250; Terms And Conditions</li>
        <li>&#8250; Support Forum</li>
      </ul>
    </div>
    <div class="footer-col">
      <h4>Send a Message</h4>
      <div class="field">Full Name</div>
      <div class="field">Your Email</div>
      <div class="field area">Message</div>
      <span class="btn submit">Submit</span>
    </div>
    <div class="footer-col">
      <h4>Get in Touch</h4>
      <p class="touch-lead">Lorem ipsum dolor sit amet, consectetuer adipiscing elit.</p>
      <div class="touch-row">
        <svg width="9" height="12" viewBox="0 0 12 16"><path d="M6 0a6 6 0 0 0-6 6c0 4 6 10 6 10s6-6 6-10a6 6 0 0 0-6-6z" fill="#9a9a9a"/><circle cx="6" cy="6" r="2.2" fill="#0d0d0d"/></svg>
        <span>Cedar Court, 18 Mill Lane, Westbrook</span>
      </div>
      <div class="touch-row">
        <svg width="10" height="10" viewBox="0 0 13 13"><path d="M3 0 5 3 3.5 4.5c.8 2 2.5 3.7 4.5 4.5L9.5 7.5 13 9.5 12 12C6 12 1 7 1 1z" fill="#9a9a9a"/></svg>
        <span>+410 555.201.774</span>
      </div>
      <div class="touch-row">
        <svg width="11" height="8" viewBox="0 0 13 10"><rect width="13" height="10" rx="1" fill="#9a9a9a"/><path d="m1 1 5.5 4.5L12 1" stroke="#0d0d0d" fill="none"/></svg>
        <span>support@northvalerealty.com</span>
      </div>
      <div class="touch-row">
        <svg width="10" height="10" viewBox="0 0 10 10" fill="none" stroke="#9a9a9a"><circle cx="5" cy="5" r="4.3"/><path d="M.7 5h8.6M5 .7c2 2.4 2 6.2 0 8.6M5 .7c-2 2.4-2 6.2 0 8.6"/></svg>
        <span>www.northvalerealty.com</span>
      </div>
    </div>
  </div>
  <div class="copyright">Copyright © 2016 Northvale-Realty-Services</div>
</footer>

</body>
</html>
```